Bakery Business Cards

We are in need of business cards for our bakery business--something non-generic that reflects our business and will stand out. We are a wholesale bakery that primarily services in-store bakeries, casinos, schools, distributors, and fund-raising companies. The family business was founded in 1960. (www.marlowsovenworks.com)

```html
<!DOCTYPE html>
<html lang="en">
<head>
<meta charset="UTF-8">
<title>Marlow's Ovenworks – Business Cards</title>
<link href="https://fonts.googleapis.com/css2?family=Montserrat:wght@400;500;600&display=swap" rel="stylesheet">
<style>
  :root {
    --backdrop: #aeafab;
    --card-white: #ffffff;
    --brand-blue: #2143a0;
    --ink-grey: #4a4a4a;
    --photo-wood: #d9b98f;
    --photo-plate: #f3efe8;
    --photo-crust: #e2c08a;
  }
  * { margin: 0; padding: 0; box-sizing: border-box; }
  html, body { width: 1200px; height: 801px; overflow: hidden; }
  body {
    background: var(--backdrop);
    font-family: 'Montserrat', sans-serif;
    display: flex;
    align-items: center;
    justify-content: center;
    gap: 40px;
  }
  .card {
    width: 525px;
    height: 300px;
    border-radius: 16px;
    position: relative;
    overflow: hidden;
    box-shadow: 0 10px 24px rgba(0,0,0,0.18);
  }
  .card-front { background: var(--card-white); }
  .brand-name {
    color: var(--brand-blue);
    font-weight: 600;
    font-family: 'Montserrat', sans-serif;
    letter-spacing: 0.5px;
  }
  .front-logo {
    position: absolute;
    top: 34px; right: 36px;
    font-size: 24px;
    text-align: right;
    line-height: 1.15;
  }
  .front-rule {
    position: absolute;
    top: 120px; left: 36px; right: 36px;
    height: 1px;
    background: var(--brand-blue);
  }
  .front-address {
    position: absolute;
    top: 134px; right: 36px;
    text-align: right;
    font-size: 12px;
    color: var(--ink-grey);
    line-height: 1.45;
  }
  .front-address .company { color: var(--brand-blue); font-weight: 600; }
  .accent-bar {
    position: absolute;
    left: 0; top: 200px;
    width: 8px; height: 38px;
    background: var(--brand-blue);
  }
  .person {
    position: absolute;
    left: 36px; top: 196px;
  }
  .person-name {
    color: var(--brand-blue);
    font-weight: 600;
    font-size: 19px;
    letter-spacing: 0.5px;
  }
  .person-title {
    font-size: 12px;
    color: var(--ink-grey);
    letter-spacing: 0.5px;
    margin-top: 2px;
  }
  .contact-rule {
    position: absolute;
    left: 36px; top: 243px;
    width: 210px; height: 1px;
    background: var(--brand-blue);
  }
  .contact-list {
    position: absolute;
    left: 36px; top: 249px;
    list-style: none;
    font-size: 10.5px;
    color: var(--ink-grey);
    line-height: 1.45;
  }
  .contact-list li { display: flex; align-items: center; gap: 6px; }
  .contact-list svg { width: 9px; height: 9px; flex: none; }
  .card-back { background: var(--photo-wood); }
  .pie-photo {
    position: absolute; inset: 0;
    background:
      radial-gradient(circle at 72% 38%, var(--photo-plate) 0 18%, transparent 19%),
      radial-gradient(circle at 22% 78%, var(--photo-plate) 0 20%, transparent 21%),
      radial-gradient(circle at 88% 72%, var(--photo-crust) 0 11%, transparent 12%),
      radial-gradient(circle at 10% 40%, var(--photo-crust) 0 10%, transparent 11%),
      linear-gradient(135deg, #e6cfae, var(--photo-wood));
    opacity: 0.75;
  }
  .back-logo {
    position: absolute;
    inset: 0;
    display: flex;
    align-items: center;
    justify-content: center;
    font-size: 40px;
    text-align: center;
    line-height: 1.1;
  }
</style>
</head>
<body>
  <section class="card card-front">
    <div class="front-logo brand-name">Marlow's<br>Ovenworks</div>
    <div class="front-rule"></div>
    <address class="front-address" style="font-style:normal">
      <div class="company">Marlow's Ovenworks, Inc.</div>
      <div>1187 Linden Ave</div>
      <div>Maple Grove, OK 73120</div>
    </address>
    <div class="accent-bar"></div>
    <div class="person">
      <div class="person-name">DANIEL HARPER</div>
      <div class="person-title">DIRECTOR</div>
    </div>
    <div class="contact-rule"></div>
    <ul class="contact-list">
      <li><svg viewBox="0 0 10 10"><path d="M2 1l2 2-1 1.2a5 5 0 0 0 2.8 2.8L7 6l2 2-1.2 1.2C4.5 9 1 5.5.8 2.2z" fill="var(--brand-blue)"/></svg>405.555.0142</li>
      <li><svg viewBox="0 0 10 10"><rect x="0.5" y="2" width="9" height="6" fill="none" stroke="var(--brand-blue)"/><path d="M.5 2l4.5 3.5L9.5 2" fill="none" stroke="var(--brand-blue)"/></svg>contact@marlowsovenworks.com</li>
      <li><svg viewBox="0 0 10 10"><circle cx="5" cy="5" r="4.3" fill="none" stroke="var(--brand-blue)"/><path d="M.7 5h8.6M5 .7c-2.5 2.5-2.5 6.1 0 8.6M5 .7c2.5 2.5 2.5 6.1 0 8.6" fill="none" stroke="var(--brand-blue)" stroke-width="0.8"/></svg>www.marlowsovenworks.com</li>
    </ul>
  </section>

  <section class="card card-back">
    <div class="pie-photo" role="img" aria-label="Overhead photo of fruit pie slices and cobblers on white plates on a wooden table"></div>
    <div class="back-logo brand-name">Marlow's<br>Ovenworks</div>
  </section>
</body>
</html>
```